Icon design for mobile app bottom tabs

Hi - we are creating a mobile app that uses icons to on the 5 bottom tabs. We are looking for a nice design for these 5 icons. Attached are:

1) Wireframe showing how the 5 icons are laid out and what they are for

2) Visual design showing our current color palette and a design option for the icons we would like to improve upon (this one only shows 4 tabs - but we would like a design for the 5 tabs as laid out in the wireframe.

3) Note that the attachments include labels, but we are open to designs that don't use labels for the icons if the icons are good and easily understood.

We would like to turn this around quickly.

```html
<!DOCTYPE html>
<html lang="en">
<head>
<meta charset="utf-8">
<title>Messages</title>
<link href="https://fonts.googleapis.com/css2?family=Arimo:wght@400;700&display=swap" rel="stylesheet">
<style>
  :root {
    --screen-bg: #e7e8ea;
    --card-bg: #ffffff;
    --ink: #333333;
    --ink-strong: #000000;
    --muted: #b3b3b3;
    --tab-muted: #9c9c9c;
    --tab-active: #444444;
    --tab-border: #c8c8c8;
    --tab-bg: #eeeeef;
    --accent: #c8232c;
    --avatar-grey: #bdbdbd;
    --bar-bg: #f5f6f8;
    --bar-line: #dcdcdc;
  }
  * { box-sizing: border-box; margin: 0; padding: 0; }
  html, body { width: 675px; height: 1200px; overflow: hidden; }
  body {
    position: relative;
    background: var(--screen-bg);
    font-family: "Arimo", Helvetica, Arial, sans-serif;
    color: var(--ink);
  }
  .status-bar {
    position: absolute; left: 0; top: 0; width: 675px; height: 35px;
    font-size: 17px; color: var(--ink-strong);
  }
  .status-left { position: absolute; left: 10px; top: 7px; display: flex; align-items: center; gap: 6px; }
  .signal { display: flex; gap: 2px; }
  .signal span { width: 9px; height: 9px; border-radius: 50%; background: var(--ink-strong); }
  .signal span.empty { background: none; border: 1px solid var(--ink-strong); }
  .status-time { position: absolute; left: 0; width: 100%; top: 7px; text-align: center; font-weight: 700; }
  .status-right { position: absolute; right: 14px; top: 8px; display: flex; align-items: center; gap: 8px; }
  .battery { width: 40px; height: 18px; border: 1.5px solid var(--ink-strong); border-radius: 3px; padding: 2px; position: relative; }
  .battery::after { content: ""; position: absolute; right: -5px; top: 5px; width: 3px; height: 6px; background: var(--ink-strong); border-radius: 0 2px 2px 0; }
  .battery i { display: block; width: 40%; height: 100%; background: var(--ink-strong); }

  .segments {
    position: absolute; left: 23px; top: 42px; width: 629px; height: 61px;
    display: flex; border: 1.5px solid var(--tab-border); border-radius: 6px; overflow: hidden;
    background: var(--tab-bg);
  }
  .segment {
    flex: 1; display: flex; align-items: center; justify-content: center; gap: 8px;
    font-size: 21px; font-weight: 700; color: var(--tab-muted);
    border-right: 1.5px solid var(--tab-border);
  }
  .segment:last-child { border-right: none; }
  .segment.active { background: var(--tab-active); color: #fff; }
  .dot { width: 11px; height: 11px; border-radius: 50%; background: var(--accent); display: inline-block; }

  .compose { position: absolute; left: 312px; top: 124px; width: 50px; height: 50px; }

  .thread {
    position: absolute; left: 16px; width: 642px; height: 103px;
    background: var(--card-bg); border-radius: 5px;
    box-shadow: 0 1px 1px rgba(0,0,0,0.06);
  }
  .thread-1 { top: 194px; }
  .thread-2 { top: 309px; }
  .thread-3 { top: 423px; }
  .avatar {
    position: absolute; left: 17px; top: 15px; width: 72px; height: 72px; border-radius: 50%;
    display: flex; align-items: center; justify-content: center;
  }
  .avatar.person { background: var(--avatar-grey); }
  .avatar.brand, .avatar.pin { background: var(--accent); }
  .thread-body { position: absolute; left: 106px; top: 17px; width: 440px; }
  .sender { font-size: 19.5px; font-weight: 700; color: var(--ink); line-height: 24px; }
  .preview { font-size: 19.5px; color: var(--ink); line-height: 26px; white-space: nowrap; overflow: hidden; text-overflow: ellipsis; }
  .time { font-size: 15px; color: var(--muted); line-height: 26px; display: flex; align-items: center; gap: 8px; }
  .time .dot { width: 10px; height: 10px; }
  .thumb { position: absolute; right: 14px; top: 15px; width: 74px; height: 73px; border-radius: 3px; }
  .thumb.workshop { background: linear-gradient(135deg, #d9c77a 0%, #8c6a45 55%, #3b2f2a 100%); }
  .thumb.card-art { background: #ee5a78; }

  .tab-bar {
    position: absolute; left: 0; top: 1120px; width: 675px; height: 80px;
    background: var(--bar-bg); border-top: 1px solid var(--bar-line);
    display: flex; justify-content: space-around; align-items: center; padding: 0 18px;
  }
  .tab-icon { width: 64px; height: 52px; display: flex; align-items: center; justify-content: center; }
</style>
</head>
<body>
  <header class="status-bar">
    <div class="status-left">
      <div class="signal"><span></span><span></span><span></span><span></span><span class="empty"></span></div>
      <span>Nova</span><span>&nbsp;LTE</span>
    </div>
    <div class="status-time">4:15 PM</div>
    <div class="status-right">
      <svg width="14" height="14" viewBox="0 0 14 14"><path d="M13 1 L1 6 L7 7 L8 13 Z" fill="#000"/></svg>
      <svg width="16" height="16" viewBox="0 0 16 16"><circle cx="8" cy="9" r="6" fill="#000"/><path d="M8 5v4l2.5 1.5" stroke="#fff" stroke-width="1.5" fill="none"/><path d="M1 3l3-2M15 3l-3-2" stroke="#000" stroke-width="2"/></svg>
      <svg width="10" height="17" viewBox="0 0 10 17"><path d="M1 5l8 7-4 3V2l4 3-8 7" stroke="#999" stroke-width="1.5" fill="none"/></svg>
      <div class="battery"><i></i></div>
    </div>
  </header>

  <nav class="segments">
    <div class="segment">News</div>
    <div class="segment"><span class="dot"></span>You</div>
    <div class="segment active">Messages</div>
  </nav>

  <svg class="compose" viewBox="0 0 50 50" aria-label="New message">
    <circle cx="25" cy="25" r="25" fill="var(--accent)"/>
    <path d="M25 13v24M13 25h24" stroke="#fff" stroke-width="4.5" stroke-linecap="round"/>
  </svg>

  <article class="thread thread-1">
    <div class="avatar person">
      <svg width="30" height="32" viewBox="0 0 30 32"><circle cx="15" cy="9" r="8" fill="#fff"/><path d="M0 32v-6c0-5 4-8 9-8h12c5 0 9 3 9 8v6z" fill="#fff"/></svg>
    </div>
    <div class="thread-body">
      <div class="sender">danmercer2010@mailbox.com</div>
      <div class="preview">What's up?</div>
      <div class="time">1 month ago</div>
    </div>
  </article>

  <article class="thread thread-2">
    <div class="avatar brand"></div>
    <div class="thread-body">
      <div class="sender">Corkly</div>
      <div class="preview">You can send messages to your friends! Pl…</div>
      <div class="time"><span class="dot"></span>8 months ago</div>
    </div>
    <div class="thumb workshop" role="img" aria-label="Photo of people working at a table"></div>
  </article>

  <article class="thread thread-3">
    <div class="avatar pin">
      <svg width="28" height="40" viewBox="0 0 28 40"><path d="M7 2h14l-2 3v9l7 8H2l7-8V5z" fill="#fff"/><rect x="12.5" y="22" width="3" height="16" fill="#fff"/></svg>
    </div>
    <div class="thread-body">
      <div class="sender">Maya Tindall</div>
      <div class="preview">Test</div>
      <div class="time">1 year ago</div>
    </div>
    <div class="thumb card-art" role="img" aria-label="Pink greeting card illustration with a caption"></div>
  </article>

  <footer class="tab-bar">
    <div class="tab-icon" aria-label="My photos">
      <svg width="60" height="44" viewBox="0 0 60 44">
        <rect x="2" y="2" width="50" height="36" fill="none" stroke="#000" stroke-width="4"/>
        <path d="M6 34l12-14 9 9 6-5 12 10z" fill="#000"/>
        <circle cx="40" cy="12" r="4" fill="#000"/>
        <circle cx="46" cy="32" r="12" fill="#000" stroke="#f5f6f8" stroke-width="2"/>
        <circle cx="46" cy="28" r="4" fill="#fff"/>
        <path d="M38 39c1-5 4-6 8-6s7 1 8 6" fill="#fff"/>
      </svg>
    </div>
    <div class="tab-icon" aria-label="Add photo">
      <svg width="60" height="44" viewBox="0 0 60 44">
        <rect x="2" y="2" width="50" height="36" fill="none" stroke="#000" stroke-width="4"/>
        <path d="M6 34l12-14 9 9 6-5 12 10z" fill="#000"/>
        <circle cx="40" cy="12" r="4" fill="#000"/>
        <circle cx="46" cy="32" r="11" fill="#000" stroke="#f5f6f8" stroke-width="2"/>
        <path d="M46 26v12M40 32h12" stroke="#fff" stroke-width="3"/>
      </svg>
    </div>
    <div class="tab-icon" aria-label="Camera">
      <svg width="54" height="44" viewBox="0 0 54 44">
        <path d="M4 8h12l4-6h14l4 6h12a3 3 0 0 1 3 3v29a3 3 0 0 1-3 3H4a3 3 0 0 1-3-3V11a3 3 0 0 1 3-3z" fill="#000"/>
        <circle cx="27" cy="25" r="11" fill="#fff"/>
        <circle cx="27" cy="25" r="7" fill="#000"/>
      </svg>
    </div>
    <div class="tab-icon" aria-label="Add friends">
      <svg width="64" height="46" viewBox="0 0 64 46">
        <circle cx="36" cy="10" r="9" fill="#000"/>
        <path d="M22 40c0-11 6-17 14-17s14 6 14 17z" fill="#000"/>
        <circle cx="16" cy="14" r="7.5" fill="#000" stroke="#f5f6f8" stroke-width="2"/>
        <path d="M2 40c0-9 5-14 13-14s13 5 13 14z" fill="#000" stroke="#f5f6f8" stroke-width="2"/>
        <circle cx="52" cy="36" r="9.5" fill="#000" stroke="#f5f6f8" stroke-width="2"/>
        <path d="M52 31v10M47 36h10" stroke="#fff" stroke-width="2.5"/>
      </svg>
    </div>
    <div class="tab-icon" aria-label="Settings">
      <svg width="48" height="48" viewBox="0 0 48 48">
        <circle cx="24" cy="24" r="18" fill="none" stroke="#000" stroke-width="8" stroke-dasharray="5.9 3.5"/>
        <circle cx="24" cy="24" r="15" fill="#000"/>
        <circle cx="24" cy="24" r="7" fill="#f5f6f8"/>
      </svg>
    </div>
  </footer>
</body>
</html>
```